BRIGHTWAVE PARTNERS NAMECARD

Need to design a name card with an existing logo.

As we are professional corporate services provider our name card has to project a professional image.
Should be corporate, simple & professional.

Our corporate color is maroon red but not too dull.

Please refer to our website at www.brightwavepartners.com.sg

Would attach our logo herewith.

Front surface of namecard details:
BRIGHTWAVE PARTNERS PTE LTD
Registration No. 208731945K

Lowe Hui Ting CA (Singapore)
Director

Tel +65 6481 2957
Mobile +65 9172 3806
lowe@brightwavepartners.com.sg
www.brightwavepartners.com.sg

47 Palmer Lane
#07-14 Harbourlight Plaza
Singapore 274153

Back of namecard:-
OUR CORE SERVICES
Incorporation services
Corporate Secretarial Services
Accountancy service
Goods & Services Taxation
Corporate & Personal Taxation
Financial Reporting
Payroll Administration

AFFILIATES:
TRIVANTA CORPORATE SERVICES PTE LTD
BRIGHTWAVEREGISTRYPTE LTD
ORR MANAGEMENT SERVICES PTE LTD
DW LIM AND COMPANY PTE LTD
LEDGERWISE ACADEMY

```html
<!DOCTYPE html>
<html lang="en">
<head>
<meta charset="utf-8">
<title>Brightwave Partners Name Card</title>
<link rel="stylesheet" href="https://fonts.googleapis.com/css2?family=Open+Sans:ital,wght@0,400;0,600;0,700;1,700&display=swap">
<style>
  :root {
    --brand-red: #d11f33;
    --paper: #ffffff;
    --soft-grey: #d9d9d9;
    --backdrop: #3a3a3a;
    --font-text: "Open Sans", Arial, sans-serif;
  }
  * { box-sizing: border-box; margin: 0; padding: 0; }
  html, body { width: 1200px; height: 900px; overflow: hidden; }
  body {
    background: var(--backdrop);
    font-family: var(--font-text);
    position: relative;
  }
  .card {
    position: absolute;
    left: 240px;
    width: 720px;
    height: 410px;
    overflow: hidden;
  }
  .card-back { top: 30px; background: var(--brand-red); color: var(--paper); }
  .card-front { top: 460px; background: var(--brand-red); color: var(--paper); }

  .wordmark {
    font-family: var(--font-text);
    font-weight: 700;
    text-transform: uppercase;
    line-height: 0.95;
    letter-spacing: 1px;
    white-space: nowrap;
  }
  .card-back .wordmark {
    position: absolute; left: 70px; top: 30px;
    font-size: 54px; color: var(--paper);
  }
  .affiliates {
    position: absolute; left: 50px; top: 200px;
    font-size: 13px; line-height: 1.4; text-transform: uppercase;
  }
  .affiliates h3, .services h3 {
    font-size: 14px; font-weight: 700; font-style: italic;
  }
  .card-list { list-style: none; }
  .card-list li::before { content: "\2022"; margin-right: 6px; }
  .services {
    position: absolute; left: 440px; top: 220px;
    font-size: 15px; line-height: 1.35;
  }
  .services h3 { font-size: 16px; font-style: normal; text-transform: uppercase; }

  .front-art { position: absolute; inset: 0; }
  .card-front .wordmark {
    position: absolute; left: 412px; top: 145px;
    font-size: 41px; color: var(--brand-red);
  }
  .contact {
    position: absolute; left: 40px; top: 32px;
    font-size: 15px; line-height: 1.35;
  }
  .contact-name { font-size: 21px; font-weight: 700; }
  .contact-cred { font-size: 14px; font-weight: 700; }
  .contact-address { margin: 10px 0 10px; }
  .contact-line { display: flex; align-items: center; gap: 8px; }
  .contact-line svg { width: 14px; height: 14px; flex: none; }
  .company {
    margin-top: 12px;
    font-size: 12px; line-height: 1.4;
  }
  .company-name { font-weight: 700; }
</style>
</head>
<body>

<section class="card card-back" aria-label="Name card back">
  <div class="wordmark">Brightwave<br>Partners</div>

  <div class="affiliates">
    <h3>AFFILIATES</h3>
    <ul class="card-list">
      <li>TRIVANTA CORPORATE SERVICES PTE LTD</li>
      <li>BRIGHTWAVEREGISTRYPTE LTD</li>
      <li>ORR MANAGEMENT SERVICES PTE LTD</li>
      <li>DW LIM AND COMPANY PTE LTD</li>
      <li>LEDGERWISE ACADEMY</li>
    </ul>
  </div>

  <div class="services">
    <h3>Our Core Services</h3>
    <ul class="card-list">
      <li>Incorporation services</li>
      <li>Corporate Secretarial Services</li>
      <li>Accountancy service</li>
      <li>Goods Services Taxation</li>
      <li>Corporate Personal Taxation</li>
      <li>Financial Reporting</li>
      <li>Payroll Administration</li>
    </ul>
  </div>
</section>

<section class="card card-front" aria-label="Name card front">
  <svg class="front-art" viewBox="0 0 720 410" aria-hidden="true">
    <path d="M400 0 Q300 200 340 410 L720 410 L720 0 Z" fill="var(--soft-grey)"/>
    <path d="M440 0 Q330 200 360 410 L720 410 L720 0 Z" fill="var(--brand-red)"/>
    <path d="M470 0 Q345 200 372 410 L720 410 L720 0 Z" fill="var(--paper)"/>
  </svg>

  <div class="contact">
    <div class="contact-name">Lowe Hui Ting CA</div>
    <div class="contact-cred">(Singapore)</div>
    <div class="contact-role">Director</div>
    <div class="contact-address">
      47 Palmer Lane<br>
      #07-14 Harbourlight Plaza<br>
      Singapore 274153
    </div>
    <div class="contact-line">
      <svg viewBox="0 0 16 16"><path fill="#fff" d="M3 1l3 3-1.5 2a9 9 0 0 0 5.5 5.5L12 10l3 3-2 2C7 15 1 9 1 3z"/></svg>
      +65 6481 2957
    </div>
    <div class="contact-line">
      <svg viewBox="0 0 16 16"><rect x="4" y="1" width="8" height="14" rx="1.5" fill="none" stroke="#fff" stroke-width="1.5"/><circle cx="8" cy="12.5" r="1" fill="#fff"/></svg>
      +65 9172 3806
    </div>
    <div class="contact-line">
      <svg viewBox="0 0 16 16"><rect x="1" y="3" width="14" height="10" fill="#fff"/><path d="M1 3l7 6 7-6" fill="none" stroke="var(--brand-red)" stroke-width="1.2"/></svg>
      lowe@brightwavepartners.com.sg
    </div>
    <div class="contact-line">
      <svg viewBox="0 0 16 16"><circle cx="8" cy="8" r="7" fill="#fff"/><path d="M1 8h14M8 1c-3 4-3 10 0 14M8 1c3 4 3 10 0 14" fill="none" stroke="var(--brand-red)" stroke-width="1"/></svg>
      www.brightwavepartners.com.sg
    </div>
    <div class="company">
      <div class="company-name">BRIGHTWAVE PARTNERS PTE LTD</div>
      <div class="company-reg">Registration No. 208731945K</div>
    </div>
  </div>

  <div class="wordmark">Brightwave<br>Partners</div>
</section>

</body>
</html>
```